label design for soy candle

I am a start up making soy candles and other products involving scents.
On the label should be in writing : Wild Rose, Handgemacht in der Schweiz, Sojakerze, my logo with the name Thorvel Candles on it. I will upload the currant label of my candles, but I want something more fashioned. The color of the label should be black with Wild Rose written in gold, and the rest in white. Or maybe suggest something different, I am open to new designs. I am also open to change the logo, except the flower has to stay.
Sizes : square 60x60mm / round 50mm / rectangle 70x20mm ( for different jars )

```html
<!DOCTYPE html>
<html lang="de">
<head>
<meta charset="utf-8">
<title>Thorvel Candles – Etikett Sojakerze</title>
<link rel="stylesheet" href="https://fonts.googleapis.com/css2?family=Dancing+Script:wght@700&family=Oswald:wght@500&family=Playfair+Display:wght@400&display=swap">
<style>
  :root {
    --backdrop: #cbcac3;
    --label-black: #0c0d10;
    --label-white: #ffffff;
    --gold-deep: #7a4a17;
    --gold-mid: #b07a3a;
    --gold-light: #e6c08a;
  }
  * { margin: 0; padding: 0; box-sizing: border-box; }
  html, body {
    width: 1200px;
    height: 700px;
    overflow: hidden;
    background: var(--backdrop);
  }
  .canvas {
    width: 1200px;
    height: 700px;
    display: flex;
    align-items: center;
    justify-content: center;
  }
  .label-round {
    width: 620px;
    height: 620px;
    display: block;
  }
  .label-disc { fill: var(--label-black); }
  .brand-name {
    font-family: "Oswald", sans-serif;
    font-weight: 500;
    font-size: 34px;
    letter-spacing: 3px;
    fill: var(--label-white);
  }
  .brand-dot { fill: var(--label-white); }
  .scent-name {
    font-family: "Dancing Script", cursive;
    font-weight: 700;
    font-size: 140px;
  }
  .origin-line {
    font-family: "Playfair Display", serif;
    font-size: 23px;
    letter-spacing: 1.5px;
    fill: var(--label-white);
  }
</style>
</head>
<body>
<main class="canvas">
  <svg class="label-round" viewBox="-310 -310 620 620" xmlns="http://www.w3.org/2000/svg">
    <defs>
      <clipPath id="disc-clip">
        <circle r="310"/>
      </clipPath>
      <linearGradient id="gold-foil" x1="0" y1="0" x2="1" y2="0.4">
        <stop offset="0" stop-color="var(--gold-deep)"/>
        <stop offset="0.45" stop-color="var(--gold-mid)"/>
        <stop offset="0.75" stop-color="var(--gold-light)"/>
        <stop offset="1" stop-color="var(--gold-mid)"/>
      </linearGradient>
      <radialGradient id="floral-tone" cx="0.5" cy="0.5" r="0.6">
        <stop offset="0" stop-color="#5a4020" stop-opacity="0.45"/>
        <stop offset="1" stop-color="#2a2012" stop-opacity="0.1"/>
      </radialGradient>
      <path id="origin-arc" d="M -262 0 A 262 262 0 0 0 262 0"/>
    </defs>

    <circle class="label-disc" r="310"/>

    <g class="floral-sprays" clip-path="url(#disc-clip)">
      <path role="img" aria-label="Goldene Magnolienzweige in Linienzeichnung, links"
            d="M -305 -20 C -295 -120 -260 -200 -225 -210 C -195 -160 -150 -120 -150 -60 C -150 0 -185 50 -225 85 C -260 105 -300 100 -315 85 Z"
            fill="url(#floral-tone)"/>
      <path role="img" aria-label="Goldene Magnolienzweige in Linienzeichnung, rechts"
            d="M 305 -20 C 300 -130 270 -215 235 -220 C 200 -160 150 -120 145 -60 C 145 0 185 50 225 85 C 260 105 300 100 315 85 Z"
            fill="url(#floral-tone)"/>
    </g>

    <g class="brand-mark">
      <circle class="brand-dot" cx="0" cy="-232" r="22"/>
      <text class="brand-name" x="0" y="-155" text-anchor="middle">THORVEL CANDLES</text>
    </g>

    <g class="scent-title" fill="url(#gold-foil)">
      <text class="scent-name" x="0" y="30" text-anchor="middle">Wild</text>
      <text class="scent-name" x="0" y="145" text-anchor="middle">Rose</text>
    </g>

    <text class="origin-line">
      <textPath href="#origin-arc" startOffset="50%" text-anchor="middle">HANDGEMACHT IN DER SCHWEIZ, SOJAKERZE</textPath>
    </text>
  </svg>
</main>
</body>
</html>
```